Business card for Sports Apparel business

DOUBLE SIDED DESIGN
We need business cards for a new sports apparel business. We are developing a protective headband for soccer initially.
Quorvane is focused on designing and developing head protection products to reduce the likelihood of concussion when playing sports. Exploring and understanding medical insights, material science research, current and former players experiences and governing bodies guidelines has allowed Quorvane to develop the safety, style, form and function requirements of a suitable product to bring to market.
Target Market(s)
Mums buying kits for the sons and daughters. Amateur footballers.
Industry/Entity Type
Sporting Good
Contact Information for Business Card
Martin Ellwood - CEO
Mobile: +44 7700123456
Email: martin@quorvane.co.uk
Tel: 0208 1234567
Rosalind Pyke - COO
Mob: +44 7700 654321
Email: rosalind@quorvane.co.uk
Tel: 0208 1234567
Gordon Haley - CCO
Mob: +44 7700 987654
Email: gordon@quorvane.co.uk
Tel: 0208 1234567
Look and feel
Each slider illustrates characteristics of the customer's brand and the style your logo design should communicate.

```html
<!DOCTYPE html>
<html lang="en">
<head>
<meta charset="utf-8">
<title>Quorvane business cards</title>
<link rel="stylesheet" href="https://fonts.googleapis.com/css2?family=Montserrat:wght@600;700&family=Roboto:wght@400&display=swap">
<style>
:root{
  --brand-blue:#1a6096;
  --ink:#1b1b1b;
  --muted:#6d6d6d;
  --icon:#8a8a8a;
  --stage:#c8c8c8;
  --paper:#ffffff;
}
*{box-sizing:border-box;margin:0;padding:0}
html,body{width:1200px;height:2353px;overflow:hidden;background:var(--paper)}
.stage{position:absolute;left:0;top:0;width:1200px;height:1200px;background:var(--stage)}
.sheet{position:absolute;left:0;top:1200px;width:1200px;height:1153px;background:var(--paper)}
.card{
  --u:1px;
  position:absolute;
  width:calc(500*var(--u));
  height:calc(324*var(--u));
}
.card--large{--u:1.24px}
.card--front{background:var(--paper);box-shadow:0 0 0 1px #d4d4d4,1px 2px 4px rgba(0,0,0,.25)}
.card--back{background:var(--brand-blue)}
.wordmark{
  position:absolute;
  font-family:"Montserrat",sans-serif;
  font-weight:600;
  letter-spacing:.02em;
  line-height:1;
  white-space:nowrap;
}
.card--front .wordmark{left:calc(24*var(--u));top:calc(27*var(--u));font-size:calc(29*var(--u));color:var(--brand-blue)}
.card--back .wordmark{left:50%;top:50%;transform:translate(-50%,-50%);font-size:calc(50*var(--u));color:var(--paper)}
.person{position:absolute;left:calc(24*var(--u));top:calc(200*var(--u))}
.person__name{font-family:"Montserrat",sans-serif;font-weight:700;font-size:calc(20*var(--u));color:var(--ink);line-height:1.2}
.person__role{font-family:"Montserrat",sans-serif;font-weight:600;font-size:calc(13*var(--u));color:var(--muted);line-height:1.4}
.contacts{position:absolute;left:calc(239*var(--u));top:calc(203*var(--u));list-style:none}
.contacts li{
  display:flex;align-items:center;
  height:calc(23*var(--u));
  font-family:"Roboto",sans-serif;font-size:calc(17*var(--u));color:var(--ink);
}
.contacts svg{width:calc(18*var(--u));height:calc(18*var(--u));margin-right:calc(6*var(--u));fill:none;stroke:var(--icon);stroke-width:1.2}
</style>
</head>
<body>
<svg width="0" height="0" style="position:absolute">
  <defs>
    <symbol id="icon-mobile" viewBox="0 0 18 18"><rect x="5" y="1" width="8" height="16" rx="1.2"/><line x1="8" y1="15" x2="10" y2="15"/></symbol>
    <symbol id="icon-phone" viewBox="0 0 18 18"><path d="M4 2l3 3-1.5 2c1 2 3 4 5 5l2-1.5 3 3-2 2C8 15 3 10 2 4z"/></symbol>
    <symbol id="icon-mail" viewBox="0 0 18 18"><rect x="1.5" y="4" width="15" height="10"/><path d="M1.5 4l7.5 6 7.5-6"/></symbol>
    <symbol id="icon-web" viewBox="0 0 18 18"><circle cx="9" cy="9" r="7.5"/><ellipse cx="9" cy="9" rx="3.2" ry="7.5"/><line x1="1.5" y1="9" x2="16.5" y2="9"/><path d="M3 5h12M3 13h12"/></symbol>
  </defs>
</svg>

<section class="stage">
  <div class="card card--back card--large" style="left:60px;top:150px"><span class="wordmark">QUORVANE</span></div>
  <div class="card card--front card--large" style="left:520px;top:630px">
    <span class="wordmark">QUORVANE</span>
    <div class="person"><p class="person__name">Martin Ellwood</p><p class="person__role">CEO</p></div>
    <ul class="contacts">
      <li><svg><use href="#icon-mobile"/></svg>+44 7700123456</li>
      <li><svg><use href="#icon-phone"/></svg>0208 1234567</li>
      <li><svg><use href="#icon-mail"/></svg>martin@quorvane.co.uk</li>
      <li><svg><use href="#icon-web"/></svg>www.quorvane.co.uk</li>
    </ul>
  </div>
</section>

<section class="sheet">
  <div class="card card--front" style="left:87px;top:69px">
    <span class="wordmark">QUORVANE</span>
    <div class="person"><p class="person__name">Martin Ellwood</p><p class="person__role">CEO</p></div>
    <ul class="contacts">
      <li><svg><use href="#icon-mobile"/></svg>+44 7700123456</li>
      <li><svg><use href="#icon-phone"/></svg>0208 1234567</li>
      <li><svg><use href="#icon-mail"/></svg>martin@quorvane.co.uk</li>
      <li><svg><use href="#icon-web"/></svg>www.quorvane.co.uk</li>
    </ul>
  </div>
  <div class="card card--back" style="left:613px;top:69px"><span class="wordmark">QUORVANE</span></div>

  <div class="card card--front" style="left:87px;top:419px">
    <span class="wordmark">QUORVANE</span>
    <div class="person"><p class="person__name">Rosalind Pyke</p><p class="person__role">COO</p></div>
    <ul class="contacts">
      <li><svg><use href="#icon-mobile"/></svg>+44 7700 654321</li>
      <li><svg><use href="#icon-phone"/></svg>0208 1234567</li>
      <li><svg><use href="#icon-mail"/></svg>rosalind@quorvane.co.uk</li>
      <li><svg><use href="#icon-web"/></svg>www.quorvane.co.uk</li>
    </ul>
  </div>
  <div class="card card--back" style="left:613px;top:419px"><span class="wordmark">QUORVANE</span></div>

  <div class="card card--front" style="left:87px;top:769px">
    <span class="wordmark">QUORVANE</span>
    <div class="person"><p class="person__name">Gordon Haley</p><p class="person__role">CCO</p></div>
    <ul class="contacts">
      <li><svg><use href="#icon-mobile"/></svg>+44 7700 987654</li>
      <li><svg><use href="#icon-phone"/></svg>0208 1234567</li>
      <li><svg><use href="#icon-mail"/></svg>gordon@quorvane.co.uk</li>
      <li><svg><use href="#icon-web"/></svg>www.quorvane.co.uk</li>
    </ul>
  </div>
  <div class="card card--back" style="left:613px;top:769px"><span class="wordmark">QUORVANE</span></div>
</section>
</body>
</html>
```